Wild Ridge Trekcraft DL flyer

I'm looking for a new flyer for my startup business. In Darwin Australia.
Aimed at family's and short stay tourists the "Wild Ridge Trekcraft" 4 hr tour will give people a basic understanding of some essential bush survival skills in the Australian Outback.
things covered in this 4 hr tour are
1. Finding water.
2. finding food.
3. Finding/making shelter and fire.
4. Finding your way home.

The tour will pick clients up in an air conditioned purpose build 4WD and take them to a nearby bushland area where they will have the opportunity to catch and harvest some native bushtucker.
They will then be able to find/harvest some water for survival situations.
While we cook our bush tucker they will also learn to find their way home through ancient navigation techniques as well.

Clients will then be dropped back to their accomodation with some fun and vital knowledge of surviving in the Australian outback.
At the end of the tour the group will be able to take home a basic survival kit which they will be able to use through the skills they just gained on the tour.

I'd like a two sided DL size flyer emphasising the following points.
4hr/half day tour
Fun for the family
Free survival kit included.
Eat what you catch
Learn essential survival skills
Provided buy an experienced and passionate bushman.
$150/head including transfers.

I'll provide some pictures for the flyer and any extra content you require.
Updates

Target Market(s)

Family's
Short stay tourists

Industry/Entity Type

Tourism

Colors

Designer to choose colors to be used in the design.

Requirements
Must have
• As per brief
Nice to have
• Any extra content and flair designers would like to add
Should not have
• Any images which aren't Australian

```html
<!DOCTYPE html>
<html lang="en">
<head>
<meta charset="utf-8">
<title>Wild Ridge Trekcraft DL flyer</title>
<link rel="stylesheet" href="https://fonts.googleapis.com/css2?family=Oswald:wght@500;600;700&family=Montserrat:wght@400;500&display=swap">
<style>
:root{
  --stage:#111111;
  --green:#4a7a10;
  --green-light:#6a9a25;
  --green-deep:#233410;
  --olive:#6b6a1c;
  --olive-dark:#4b6b12;
  --gold:#f5c15a;
  --white:#ffffff;
  --grey:#ebebeb;
  --brown:#332a1e;
  --rust:#7a3212;
  --ink:#1d1d1d;
}
*{margin:0;padding:0;box-sizing:border-box}
html,body{width:1100px;height:1200px;overflow:hidden;background:var(--stage)}
body{position:relative;font-family:"Montserrat",sans-serif}
.panel{position:absolute;top:200px;width:377px;height:800px;overflow:hidden}
.panel--front{left:150px;background:var(--green)}
.panel--back{left:573px;background:var(--grey)}
.photo{position:absolute}
.front-header{position:absolute;left:0;top:0;width:377px;height:129px;background:var(--white);text-align:center}
.call-label{position:absolute;left:0;right:0;top:30px;font-size:29px;color:var(--olive-dark);letter-spacing:1px;font-weight:400}
.call-number{position:absolute;left:0;right:0;top:62px;font-family:"Oswald",sans-serif;font-weight:700;font-size:42px;color:var(--olive);letter-spacing:1px}
.brand-title{position:absolute;left:0;right:0;top:440px;text-align:center;font-family:"Oswald",sans-serif;font-weight:700;font-size:52px;line-height:50px;letter-spacing:1px}
.brand-title .line-one{color:var(--white);display:block}
.brand-title .line-two{color:var(--gold);display:block}
.feature-list{position:absolute;left:62px;top:548px;list-style:none;color:var(--white);font-size:16px;line-height:20px}
.feature-list li{position:relative;padding-left:14px;margin-bottom:4px}
.feature-list li::before{content:"";position:absolute;left:0;top:7px;width:6px;height:6px;border-radius:50%;background:var(--gold)}
.front-footer{position:absolute;left:0;bottom:0;width:377px;height:40px;background:var(--green-deep);color:var(--white);text-align:center;line-height:40px;font-size:16px;letter-spacing:.5px}
.tour-block{position:absolute;left:0;top:0;width:377px;height:285px;background:linear-gradient(135deg,var(--green-light),var(--green) 60%);color:var(--white);padding:30px 14px 0 16px}
.tour-heading{font-family:"Oswald",sans-serif;font-weight:600;font-size:23px;letter-spacing:.3px;margin-bottom:10px}
.tour-copy{font-size:11px;line-height:14.6px;margin-bottom:9px}
.compass-label{position:absolute;font-family:"Oswald",sans-serif;font-weight:700;color:var(--white);font-size:20px}
.back-call{position:absolute;left:173px;width:176px;top:634px;text-align:center}
.back-call .call-label{position:static;font-size:16px;color:var(--ink);letter-spacing:.5px}
.back-call .call-number{position:static;display:block;font-size:23px;color:var(--rust);margin-top:0}
.back-footer{position:absolute;left:0;bottom:0;width:377px;height:105px;background:var(--brown);color:var(--white);text-align:center;line-height:105px;font-size:16px}
</style>
</head>
<body>

<section class="panel panel--front">
  <header class="front-header">
    <p class="call-label">CALL US TODAY</p>
    <p class="call-number">+123 456 7890</p>
  </header>

  <div class="photo" role="img" aria-label="Termite mounds in outback grassland" style="left:0;top:129px;width:230px;height:158px;background:linear-gradient(180deg,#6f9a3e 0%,#7e8a3a 45%,#9a5a2a 70%,#5f8a28 100%)"></div>
  <div class="photo" role="img" aria-label="Bushman holding a freshly caught mud crab" style="left:234px;top:129px;width:143px;height:134px;background:linear-gradient(160deg,#5c7a3a,#9a6a4a 55%,#3e4a3a)"></div>
  <div class="photo" role="img" aria-label="Plastic bag tied over leaves collecting water" style="left:0;top:289px;width:116px;height:121px;background:linear-gradient(160deg,#3d6a2a,#9ab0a0 55%,#4a6a30)"></div>
  <div class="photo" role="img" aria-label="Hand holding wild green bush fruits" style="left:118px;top:289px;width:112px;height:121px;background:linear-gradient(160deg,#c9b59a,#6f9a3a 55%,#b89a80)"></div>
  <div class="photo" role="img" aria-label="Freshwater crayfish held in open hands" style="left:234px;top:266px;width:143px;height:144px;background:linear-gradient(160deg,#8a6a50,#5a7a8a 50%,#6a4a32)"></div>

  <h1 class="brand-title"><span class="line-one">WILD RIDGE</span><span class="line-two">TREKCRAFT</span></h1>

  <ul class="feature-list">
    <li>4hr/half day tour</li>
    <li>Fun for the family</li>
    <li>Free survival kit included</li>
    <li>Eat what you catch</li>
    <li>Learn essential survival skills</li>
    <li>Provided buy an experienced<br>and passionate bushman</li>
    <li>$150/head including transfers</li>
  </ul>

  <footer class="front-footer">WILDRIDGETREK.COM</footer>
</section>

<section class="panel panel--back">
  <div class="tour-block">
    <h2 class="tour-heading">TOUR DESCRIPTION GOES HERE?</h2>
    <p class="tour-copy">The tour will pick clients up in an air conditioned purpose build 4WD and take them to a nearby bushland area where they will have the opportunity to catch and harvest some native bushtucker. They will then be able to find/harvest some water for survival situations. While we cook our bush tucker they will also learn to find their way home through ancient navigation techniques as well.</p>
    <p class="tour-copy">Clients will then be dropped back to their accomodation with some fun and vital knowledge of surviving in the Australian outback. At the end of the tour the group will be able to take home a basic survival kit which they will be able to use through the skills they just gained on the tour.</p>
  </div>

  <div class="photo" role="img" aria-label="Stick shadow navigation marked on dry earth" style="left:24px;top:295px;width:325px;height:200px;background:linear-gradient(150deg,#8a7a4a,#7a6a40 50%,#9a8a5a)"></div>
  <span class="compass-label" style="left:252px;top:341px">WEST</span>
  <span class="compass-label" style="left:45px;top:440px">EAST</span>

  <div class="photo" role="img" aria-label="Yellow bush fruit hanging on a branch" style="left:24px;top:505px;width:139px;height:179px;background:linear-gradient(160deg,#7aa0c0,#e0a020 55%,#5a4a30)"></div>
  <div class="photo" role="img" aria-label="Pandanus palm fronds" style="left:173px;top:505px;width:176px;height:118px;background:linear-gradient(160deg,#c8d8c0,#4a7a30 55%,#9aa080)"></div>

  <div class="back-call">
    <p class="call-label">CALL US TODAY</p>
    <p class="call-number">+123 456 7890</p>
  </div>

  <footer class="back-footer">Company address goes here</footer>
</section>

</body>
</html>
```